Functional Beverage- Flavoured Vitamin Water

Hi,

We need a product label design for a new flavoured vitamin water in London: "Solvenne" .

Solvenne is a refreshing vitamin infusion ready to drink beverage. It is a naturally sweetened (low sugar NOT no sugar, but free from artificial sweetners), with natural colours and flavours - with added vitamins and supplements, including natural botanicals. We want to clearly label this to be a health drink and highlight the benefits. It is a STILL drink and either CLEAR or TINTED RED depending on the flavour.

We have used leading research from the nutritional industry to create functional blends in a light refreshing water that is not sugar laden or artificially flavoured. WE TASTE GREAT!

These are the 4 flavours however for the purposes of the brief I am happy for the designers to focus on either

1. CRANBERRY RASPERRY - rose red - REDOX (contains antioxidants and help immunity)
2. COCONUT PINEAPPLE - clear - BEAUTY (helps maintain hair, skin and nails)

I want the product label to be fresh and stand out as this will be facing competition from established brands (Morvelt / K-Drink).

Labels will be printed on self-adhesive plastic and be applied to a 500 ml PET clear plastic bottle. The label itself would be no more than 190mm wide by 80mm tall and will be a rectangle (to give you an idea of scale when the consumer looks at the label).

I want something as striking, pure and playful as these two brands have on their waters (but not as minimal...)

1. http://example-quillnest.com/?p=48213
2. http://www.example-tormwick.com/energy/arch/007215.php
3. Existing bottle is here: https://example-lnk.test/QpWm83Zs

We will be relying on social media for marketing and PR so fthe design needs to transfer to that type of media well.

Thanks and good luck
Updates

Hi all,

Just a note to the invited designers - hoping some more of you can jump into the project over the weekend if you have not already submitted designs.

Thanks and regards,

Oren

Reason: Extending so we can get some more designs submitted. Thanks.

Hi,

I have increased the budget to allow for a $100 2nd prize, as we are seeing some strong designs in the closing stages.

Regards,
Oren

Reason: Collating final feedback on submissions.

Target Market(s)

18-35 yeare old professionals who consume vitamin supplements and want a ready to drink flavoured water that's different to the standard offering.

It is unisex but feel the brand may appeal more to women initially. But I dont want to disenfranchise men.

Industry/Entity Type

Marketing

Requirements
Must have
• Health benefit claims
Flavour names
Mention the natural fruit sugars and stevia
Nice to have
• Mention how it's "Low Cal not No Cal"

I like the idea of a clear or semi clear label that uses the back of the label on the opposite side like the TOKO water bottle in the attached file. This makes it looks so much more 3d than a "front" label... not a mandatory requirement - just an idea to think of.

```html
<!DOCTYPE html>
<html lang="en">
<head>
<meta charset="utf-8">
<title>Solvenne Raspberry Label</title>
<link rel="stylesheet" href="https://fonts.googleapis.com/css2?family=Quicksand:wght@400;500;600&family=Yellowtail&family=Oswald:wght@600&family=Roboto:wght@500&display=swap">
<style>
  :root {
    --page: #f3f1f3;
    --label-top: #c81d78;
    --label-bottom: #b0115f;
    --brand: #ececf0;
    --dot: #c9c4cc;
    --claim: #ffffff;
    --flavour: #e7a9d8;
    --sweetener: #ffe81a;
  }
  * { margin: 0; padding: 0; box-sizing: border-box; }
  html, body {
    width: 1200px;
    height: 2490px;
    overflow: hidden;
    background: var(--page);
  }
  .canvas {
    position: relative;
    width: 1200px;
    height: 2490px;
  }
  .label {
    position: absolute;
    left: 120px;
    top: 980px;
    width: 960px;
    height: 960px;
    background: linear-gradient(180deg, var(--label-top), var(--label-bottom));
    overflow: hidden;
  }
  .diagonal-block {
    position: absolute;
    left: 480px;
    top: 400px;
    width: 720px;
    transform: translate(-50%, -50%) rotate(40deg);
    display: flex;
    flex-direction: column;
    align-items: flex-start;
  }
  .brand {
    display: flex;
    align-items: center;
    gap: 22px;
    font-family: "Quicksand", sans-serif;
    font-weight: 500;
    font-size: 118px;
    line-height: 1;
    letter-spacing: 2px;
    color: var(--brand);
  }
  .brand-dot {
    width: 26px;
    height: 26px;
    border-radius: 50%;
    background: var(--dot);
  }
  .details {
    display: flex;
    width: 100%;
    justify-content: space-between;
    align-items: flex-start;
    margin-top: 22px;
  }
  .claim {
    font-family: "Quicksand", sans-serif;
    font-weight: 400;
    font-size: 34px;
    line-height: 1.15;
    color: var(--claim);
  }
  .volume {
    font-family: "Quicksand", sans-serif;
    font-weight: 400;
    font-size: 48px;
    line-height: 1;
    color: var(--claim);
  }
  .flavour {
    align-self: flex-end;
    margin-top: 14px;
    font-family: "Yellowtail", cursive;
    font-size: 78px;
    line-height: 1;
    color: var(--flavour);
  }
  .calorie-note {
    position: absolute;
    left: 0;
    width: 100%;
    top: 720px;
    text-align: center;
    font-family: "Roboto", sans-serif;
    font-weight: 500;
    font-size: 28px;
    color: var(--claim);
  }
  .sweetener-note {
    position: absolute;
    left: 0;
    width: 100%;
    top: 768px;
    text-align: center;
    font-family: "Oswald", sans-serif;
    font-weight: 600;
    font-size: 28px;
    letter-spacing: 0.5px;
    color: var(--sweetener);
  }
</style>
</head>
<body>
  <main class="canvas">
    <section class="label">
      <div class="diagonal-block">
        <div class="brand"><span class="brand-dot"></span>Solvenne</div>
        <div class="details">
          <p class="claim">contains antioxidants<br>and help immunity</p>
          <p class="volume">500ml</p>
        </div>
        <p class="flavour">Raspberry</p>
      </div>
      <p class="calorie-note">Low Cal not No Cal</p>
      <p class="sweetener-note">NATURAL FRUIT SUGARS AND STEVIA</p>
    </section>
  </main>
</body>
</html>
```